Business cards, stationery and report cover
For market research and marketing company in New Zealand
Simple
Rosalind Thorpe
Level 1
57 Pemberly Road
Milford
Auckland
PO Box 46-582
Auckland 0963
rosalind@lumenvex.co.nz
www.lumenvex.co.nz
From this process we are looking for business cards, letterhead, comp slip, as well as a generic cover page and inside page for our reports (e.g heading styles, footers etc). Both report pages need to be easily replicated or applied to Microsoft Word reports. We are PC users if this makes a difference.
The information for the business cards can be on the front or the back - depending on your design and what looks best. Most people would contact us by phone/cell/email.
We would like to be viewed as professional, competent, modern and well established. We don't want to look like we are an advertising agency, or quirky or too different from our competitors. However, we'd like to be eye catching and interesting! Our typical clients are intelligent managers who are over 35 years and a mixture of male and female.
Please let us know if you have any questions or would like clarification on anything.
As noted in 'Additional Comments' you can choose what details would look best on the front of the business card, and which you would recommend going on the back of the card.
This is our new logo.

```html
<!DOCTYPE html>
<html lang="en">
<head>
<meta charset="utf-8">
<title>lumenvex stationery set</title>
<link href="https://fonts.googleapis.com/css2?family=Open+Sans:wght@400;600;700&family=Lora:wght@700&display=swap" rel="stylesheet">
<style>
:root{
  --bg:#e9e7e4;
  --paper:#ffffff;
  --blue:#2f7dc1;
  --blue-dark:#1e5f9a;
  --grey:#5c5e61;
  --grey-light:#c9cbcd;
  --ink:#4a4c4f;
  --muted:#9a9c9f;
}
*{margin:0;padding:0;box-sizing:border-box}
html,body{width:1200px;height:360px;overflow:hidden;background:var(--bg);font-family:"Open Sans",Arial,sans-serif;color:var(--ink)}
.sheet,.card{position:absolute;background:var(--paper);box-shadow:0 2px 5px rgba(0,0,0,.25);overflow:hidden}
.card{width:120px;height:92px}
.card--dark{background:var(--grey)}
.card--blue{background:var(--blue)}
.wordmark{font-weight:600;color:var(--blue);letter-spacing:.2px;display:flex;align-items:center;gap:3px;line-height:1}
.wordmark::before{content:"";width:.55em;height:.55em;border-radius:50%;background:currentColor}
.wordmark--light{color:#fff}
.card .wordmark{position:absolute;font-size:13px}
.card-front .wordmark{left:28px;top:38px}
.card-back .wordmark{left:8px;top:8px;font-size:9px}
.card-back .person{position:absolute;left:8px;bottom:12px;font-size:5px;line-height:1.5}
.card-back .person strong{font-size:5.5px;color:var(--ink)}
.card-back .contact{position:absolute;right:8px;top:28px;font-size:4px;line-height:1.6;text-align:right;color:var(--muted)}
.sheet{width:173px;height:307px;top:29px}
.letterhead .wordmark{position:absolute;left:14px;top:18px;font-size:12px}
.letterhead .address{position:absolute;right:14px;top:14px;font-size:4px;line-height:1.6;text-align:right;color:var(--muted)}
.footer{position:absolute;left:14px;right:14px;bottom:10px;border-top:.5px solid var(--grey-light);padding-top:3px;font-size:3.5px;color:var(--muted);text-align:center}
.report-cover svg,.report-inside svg{position:absolute;inset:0}
.report-cover .wordmark{position:absolute;left:16px;top:22px;font-size:12px}
.report-title{position:absolute;right:14px;top:130px;text-align:right}
.report-title h1{font-family:"Lora",Georgia,serif;font-size:10px;color:var(--ink)}
.report-title p{font-size:6px;color:var(--ink);margin-top:2px}
.report-title .date{font-size:4.5px;color:var(--muted)}
.report-inside .running-head{position:absolute;right:40px;top:14px;font-size:4px;color:var(--muted)}
</style>
</head>
<body>

<div class="card card-front" style="left:24px;top:36px">
  <span class="wordmark">lumenvex</span>
</div>
<div class="card card-back" style="left:156px;top:36px">
  <span class="wordmark">lumenvex</span>
  <div class="contact">57 Pemberly Road<br>PO Box 46-582<br>Auckland 0963<br>+64 9 555 0142<br>rosalind@lumenvex.co.nz<br>www.lumenvex.co.nz</div>
  <div class="person"><strong>Rosalind Thorpe</strong><br>Research Director</div>
</div>
<div class="card card--dark card-front" style="left:24px;top:144px">
  <span class="wordmark wordmark--light">lumenvex</span>
</div>
<div class="card card--blue card-front" style="left:156px;top:144px">
  <span class="wordmark wordmark--light">lumenvex</span>
</div>

<div class="sheet letterhead" style="left:307px">
  <span class="wordmark">lumenvex</span>
  <div class="address">Level 1, 57 Pemberly Road<br>Milford, Auckland<br>PO Box 46-582<br>Auckland 0963<br>www.lumenvex.co.nz</div>
  <div class="footer">rosalind@lumenvex.co.nz &nbsp;|&nbsp; +64 9 555 0142 &nbsp;|&nbsp; www.lumenvex.co.nz</div>
</div>

<div class="sheet letterhead" style="left:499px">
  <div class="footer">lumenvex &nbsp;|&nbsp; www.lumenvex.co.nz</div>
</div>

<div class="sheet report-cover" style="left:799px">
  <svg width="173" height="307" viewBox="0 0 173 307">
    <polygon points="118,0 173,0 173,55" fill="var(--blue)"/>
    <polygon points="140,0 173,0 173,33" fill="var(--blue-dark)"/>
    <rect x="20" y="170" width="58" height="58" transform="rotate(45 49 199)" fill="var(--grey-light)"/>
    <rect x="80" y="205" width="40" height="40" transform="rotate(45 100 225)" fill="var(--grey)"/>
    <rect x="95" y="245" width="34" height="34" transform="rotate(45 112 262)" fill="var(--blue)"/>
    <polygon points="0,240 0,307 67,307" fill="var(--blue)"/>
    <defs><linearGradient id="photoTone" x1="0" y1="0" x2="1" y2="1"><stop offset="0" stop-color="#f1f2f3"/><stop offset="1" stop-color="#b9bcbf"/></linearGradient></defs>
    <rect x="14" y="205" width="62" height="46" fill="url(#photoTone)" role="img" aria-label="Photo of a keyboard and calculator on a desk"/>
  </svg>
  <span class="wordmark">lumenvex</span>
  <div class="report-title">
    <h1>Brand Research Results</h1>
    <p>Hartwell Group</p>
    <p class="date">June - March 2013</p>
  </div>
</div>

<div class="sheet report-inside" style="left:991px">
  <svg width="173" height="307" viewBox="0 0 173 307">
    <polygon points="140,0 173,0 173,33" fill="var(--blue)"/>
    <polygon points="0,280 0,307 27,307" fill="var(--blue)"/>
  </svg>
  <div class="running-head">Brand Research Results</div>
  <div class="footer">lumenvex &nbsp;|&nbsp; Page 2</div>
</div>

</body>
</html>
```